Corvelle Strategies business card

I need a business card for my new strategic consulting LLC, Corvelle Strategies. We specialize in helping people who care about broadband technology and telecommunications policy, and we're based in Washington DC. I'm looking for a card that says smart, credible, future-facing and signals a high level of expertise. It's DC, so there's clearly a limit to how crazy we can go with this card, but I am looking for a design that reflects a company that is comfortable with technology, policy, and having a little bit fun. I'm uploading my logo below, and I'd like to have it be part of the card design in some fashion.
Target Market(s)
Telecommunications and technology policy professionals
Industry/Entity Type
Technology policy
Contact Information for Business Card
Name of business, my name (Glen Mosswater), email (glen@corvellestrategies-example.com) , phone number (202-555-0148)phone number

```html
<!DOCTYPE html>
<html lang="en">
<head>
<meta charset="utf-8">
<title>Corvelle Strategies business card</title>
<link rel="stylesheet" href="https://fonts.googleapis.com/css2?family=Outfit:wght@600;700&family=Open+Sans:wght@400;600&display=swap">
<style>
  :root {
    --backdrop: #c5c9d4;
    --card-white: #ffffff;
    --brand-blue: #0b539c;
    --text-white: #ffffff;
    --shadow: rgba(40, 44, 60, 0.45);
  }
  * { margin: 0; padding: 0; box-sizing: border-box; }
  html, body {
    width: 1200px;
    height: 960px;
    overflow: hidden;
    background: var(--backdrop);
  }
  .canvas {
    position: relative;
    width: 1200px;
    height: 960px;
  }
  .card {
    position: absolute;
    box-shadow: 6px 7px 8px var(--shadow);
  }
  .card-front {
    left: 275px;
    top: 92px;
    width: 662px;
    height: 376px;
    background: var(--card-white);
  }
  .card-back {
    left: 277px;
    top: 506px;
    width: 660px;
    height: 377px;
    background: var(--brand-blue);
  }
  .wordmark {
    display: flex;
    align-items: center;
    gap: 10px;
    font-family: "Outfit", sans-serif;
    font-weight: 700;
    color: var(--brand-blue);
    white-space: nowrap;
  }
  .wordmark-dot {
    width: 14px;
    height: 14px;
    border-radius: 50%;
    background: var(--brand-blue);
    flex: none;
  }
  .card-front .wordmark {
    position: absolute;
    left: 35px;
    top: 40px;
    font-size: 32px;
  }
  .holder-name {
    position: absolute;
    left: 35px;
    top: 142px;
    font-family: "Outfit", sans-serif;
    font-weight: 600;
    font-size: 39px;
    color: var(--brand-blue);
    letter-spacing: 0.2px;
  }
  .contact-list {
    position: absolute;
    left: 38px;
    top: 222px;
    list-style: none;
    font-family: "Open Sans", sans-serif;
    font-size: 18px;
    color: var(--brand-blue);
  }
  .contact-item {
    display: flex;
    align-items: center;
    gap: 8px;
    height: 31px;
  }
  .contact-icon {
    width: 20px;
    height: 20px;
    flex: none;
  }
  .logo-panel {
    position: absolute;
    left: 151px;
    top: 138px;
    width: 358px;
    height: 82px;
    background: var(--card-white);
    display: flex;
    align-items: center;
    justify-content: center;
  }
  .logo-panel .wordmark { font-size: 34px; }
  .website {
    position: absolute;
    left: 0;
    right: 0;
    top: 252px;
    text-align: center;
    font-family: "Open Sans", sans-serif;
    font-weight: 600;
    font-size: 19px;
    letter-spacing: 0.4px;
    color: var(--text-white);
  }
</style>
</head>
<body>
<main class="canvas">
  <section class="card card-front" aria-label="Card front">
    <div class="wordmark"><span class="wordmark-dot"></span>Corvelle Strategies</div>
    <h1 class="holder-name">Glen Mosswater</h1>
    <ul class="contact-list">
      <li class="contact-item">
        <svg class="contact-icon" viewBox="0 0 20 20" aria-hidden="true">
          <rect width="20" height="20" rx="4" fill="var(--brand-blue)"/>
          <rect x="4" y="6" width="12" height="9" rx="1" fill="none" stroke="#fff" stroke-width="1.5"/>
          <path d="M4.5 6.5 L10 11 L15.5 6.5" fill="none" stroke="#fff" stroke-width="1.5"/>
        </svg>
        <span>glen@corvellestrategies-example.com</span>
      </li>
      <li class="contact-item">
        <svg class="contact-icon" viewBox="0 0 20 20" aria-hidden="true">
          <rect width="20" height="20" rx="4" fill="var(--brand-blue)"/>
          <path d="M6 4.5 L8 4.5 L9 7.5 L7.6 8.6 C8.3 10.2 9.6 11.5 11.3 12.3 L12.4 10.9 L15.5 12 L15.5 14 C15.5 14.8 14.8 15.5 14 15.5 C9 15.2 4.8 11 4.5 6 C4.5 5.2 5.2 4.5 6 4.5 Z" fill="#fff"/>
        </svg>
        <span>202-555-0148</span>
      </li>
    </ul>
  </section>

  <section class="card card-back" aria-label="Card back">
    <div class="logo-panel">
      <div class="wordmark">Corvelle Strategies</div>
    </div>
    <p class="website">www.corvellestrategies-example.com</p>
  </section>
</main>
</body>
</html>
```